Business Card Design - R.T. Custom Cabinets Ltd.

Design a business card, including a new logo for a new company in Vancouver, British Columbia, Canada.

The logo must be available as a separate file.

The card should include all company information including:
R.T. Custom Cabinets Ltd.
5826 Larkspur Avenue
Burnaby, B.C. V7K 2P9
Telehone: 604-555-0173
Fax: 604-555-0173
www.rtcustomcabinets.example

As well as individual contact information for employees:
Name
Position
Telephone
Email

The card must include a thoughtful message as well

Target Market(s)

Custom Cabinets

Industry/Entity Type

Business

Contact Information for Business Card

Important information on the front, thoughtful message on the back

Colors
fbed22
9bcb3c
0355a3
ec1f27

Requirements
Must have
• See project description
Nice to have
• images that showcase custom cabinets (european, modern and traditional) styles

```html
<!DOCTYPE html>
<html lang="en">
<head>
<meta charset="utf-8">
<title>R.T. Custom Cabinets – Business Card</title>
<link rel="stylesheet" href="https://fonts.googleapis.com/css2?family=Open+Sans:ital,wght@0,400;0,600;0,700;0,800;1,400&display=swap">
<style>
  :root {
    --backdrop: #e9e7e7;
    --card: #ffffff;
    --yellow: #fbed22;
    --green: #9bcb3c;
    --blue: #0355a3;
    --red: #ec1f27;
    --ink: #3c3c3c;
    --muted: #666666;
  }
  * { box-sizing: border-box; margin: 0; padding: 0; }
  html, body { width: 1200px; height: 799px; overflow: hidden; }
  body {
    background: var(--backdrop);
    font-family: "Open Sans", Arial, sans-serif;
    position: relative;
  }
  .card {
    position: absolute;
    width: 520px;
    height: 300px;
    background: var(--card);
    overflow: hidden;
    box-shadow: 0 6px 18px rgba(0,0,0,0.10);
  }
  .card--front { left: 50px; top: 250px; }
  .card--back  { left: 630px; top: 250px; }

  .corner-arc {
    position: absolute;
    width: 96px;
    height: 96px;
    border-radius: 50%;
    background: var(--blue);
  }
  .corner-arc--top { left: 40px; top: -48px; }
  .corner-arc--bottom { right: 36px; bottom: -48px; background: var(--red); }

  .palette-band {
    position: absolute;
    left: 0; right: 0; bottom: 0;
    height: 8px;
    display: flex;
  }
  .palette-band span { flex: 1; }
  .palette-band .band-yellow { background: var(--yellow); }
  .palette-band .band-green  { background: var(--green); }
  .palette-band .band-blue   { background: var(--blue); }
  .palette-band .band-red    { background: var(--red); }

  .wordmark {
    display: flex;
    align-items: center;
    gap: 10px;
    color: var(--blue);
    font-weight: 800;
    line-height: 0.95;
    letter-spacing: -0.5px;
  }
  .wordmark__square {
    width: 44px;
    height: 44px;
    background: var(--red);
    flex: none;
  }
  .wordmark__name { font-size: 30px; }

  .staff {
    position: absolute;
    left: 228px;
    top: 50px;
    text-align: center;
  }
  .staff__name { color: var(--red); font-weight: 700; font-size: 15px; }
  .staff__role { color: var(--muted); font-size: 10px; margin-top: 1px; }

  .card--front .wordmark { position: absolute; left: 150px; top: 102px; }

  .contact {
    position: absolute;
    right: 66px;
    top: 190px;
    text-align: right;
    color: var(--ink);
    font-size: 10.5px;
    font-style: normal;
    line-height: 1.45;
  }

  .card--back .brand-block {
    position: absolute;
    left: 0; right: 0; top: 64px;
    display: flex;
    flex-direction: column;
    align-items: center;
  }
  .services {
    margin-top: 16px;
    text-align: center;
    color: var(--ink);
    font-size: 11px;
    line-height: 1.5;
  }
  .services__sep { color: var(--green); font-weight: 700; padding: 0 4px; }
  .web-line {
    margin-top: 6px;
    font-size: 11px;
    letter-spacing: 2px;
    color: var(--ink);
  }
  .web-line__domain { color: var(--red); font-weight: 700; }
  .message {
    margin-top: 18px;
    font-size: 13px;
    font-style: italic;
    color: var(--blue);
    text-align: center;
  }
</style>
</head>
<body>

<section class="card card--front" aria-label="Business card front">
  <span class="corner-arc corner-arc--top"></span>
  <span class="corner-arc corner-arc--bottom"></span>

  <div class="staff">
    <p class="staff__name">Daniel Marchetti</p>
    <p class="staff__role">Business Manager</p>
  </div>

  <div class="wordmark">
    <span class="wordmark__square"></span>
    <span class="wordmark__name">R.T. Custom<br>Cabinets</span>
  </div>

  <address class="contact">
    5826 Larkspur Avenue, Burnaby, B.C. V7K 2P9<br>
    P: (604) 555-0148, F: 604-555-0173, E: daniel@rtcustomcabinets.example<br>
    W: www.rtcustomcabinets.example
  </address>
</section>

<section class="card card--back" aria-label="Business card back">
  <div class="brand-block">
    <div class="wordmark">
      <span class="wordmark__square"></span>
      <span class="wordmark__name">R.T. Custom<br>Cabinets</span>
    </div>
    <p class="services">
      Kitchens<span class="services__sep">-</span>Bathrooms<span class="services__sep">-</span>Offices / Libraries<br>
      Custom Wine / Spirits Storage
    </p>
    <p class="web-line">- www.<span class="web-line__domain">rtcustomcabinets</span>.example -</p>
    <p class="message">“Built by hand, made to fit the way you live.”</p>
  </div>
  <div class="palette-band">
    <span class="band-yellow"></span>
    <span class="band-green"></span>
    <span class="band-blue"></span>
    <span class="band-red"></span>
  </div>
</section>

</body>
</html>
```